Custome made to measure suit brochure

Company info
Northern Heron Supply Company Ltd.
Import and export company based in Vancouver BC, Canada.

Project Scope
We need to have a brochure developed that will help us sell our custom made to measure suits from Asia (China and India) to North America.

We are not picky on the number of pages, we are looking for a brochure that best displays the needed information.
We don’t have any pictures taken, we are hoping that stock photos can be used or the winning bid will provide the photos.
Attached is our company logo and name, the attachments has 4 or 5 examples, the logo that is being used is the logo that is red and white only.

Target market is the university or college student and young professionals.
We are looking to sell the suit based on best value. Our suit is 3 to 4 times cheaper than a custom made suit made in North America.
Custom made suits make the wearer look amazing, as compared to an off the rack suit.
Custom made suits are available from $399 and up.
Vests, shirts, pants, skirts, jackets, monogramed, horn buttons, canvas and half canvas suits, pocket squares, silk and paisley linings are all available.
Available in Wool, cotton, linen, and a cotton/cashmere blend
We want the client to call us to set up a free appointment to take their measurements
100% satisfaction or your money back.
Brochure should be easy to read and understand at a quick glance.

Target Market(s)

college, university students and young professionals

Industry/Entity Type

It Company

Contact Information for Business Card

Miles Corvath
President, Northern Heron Supply Company Ltd.
1.604.555.0192
miles@nhsco-example.ca
www.nhsco-example.ca

Font styles to use
Serif

Colors
ec1f27

Requirements
Must have
• easy to read
• professional format

```html
<!DOCTYPE html>
<html lang="en">
<head>
<meta charset="utf-8">
<title>Northern Heron Supply Co – Custom Suit Brochure</title>
<link rel="stylesheet" href="https://fonts.googleapis.com/css2?family=Oswald:wght@400;500&family=Roboto+Condensed:wght@300;400&display=swap">
<style>
:root{
  --stage:#1d1d1d;
  --crimson:#cc1e48;
  --yellow:#f3d163;
  --gold:#e8b71c;
  --orange:#eea10b;
  --ink:#1b1b1b;
  --paper:#ffffff;
  --body-grey:#4a4a4a;
}
*{margin:0;padding:0;box-sizing:border-box}
html,body{width:968px;height:1200px;overflow:hidden;background:var(--stage)}
body{position:relative;font-family:"Roboto Condensed",Arial,sans-serif}
.sheet{position:absolute;left:83px;width:814px;overflow:hidden}
.sheet--outside{top:33px;height:525px;background:var(--crimson)}
.sheet--inside{top:609px;height:527px;background:var(--paper)}
.shapes{position:absolute;inset:0;width:100%;height:100%}
.block{position:absolute}
.heading{font-family:"Oswald",Arial,sans-serif;font-weight:400;line-height:1.1}
.copy{font-weight:300;font-size:8.4px;line-height:11px;text-align:justify}
.copy p+p{margin-top:11px}
.light{color:#fff}

/* outside */
.about{left:16px;top:24px;width:175px}
.about .heading,.store .heading{font-size:20px;margin-bottom:10px}
.store{left:219px;top:133px;width:175px}
.guarantee{left:226px;top:13px;width:170px;text-align:center;font-family:"Oswald",sans-serif;font-weight:500;font-size:17px;line-height:1.15;color:var(--ink)}
.contact{left:15px;top:396px;width:200px;color:var(--ink)}
.contact .heading{font-size:17px;margin-bottom:14px}
.contact-row{display:flex;align-items:flex-start;gap:9px;font-size:9.5px;font-weight:400;line-height:1.35;margin-bottom:11px}
.contact-row svg{flex:none;width:10px;height:11px;margin-top:1px}
.photo-panel{position:absolute;left:407px;top:0;width:407px;height:525px;background:linear-gradient(180deg,#eeeff3,#d3d4d9)}
.model-photo{position:absolute;left:545px;top:0;width:255px;height:525px;background:linear-gradient(90deg,rgba(30,30,34,0) 0%,rgba(30,30,34,.85) 22%,#17171a 50%,rgba(30,30,34,.85) 78%,rgba(30,30,34,0) 100%)}
.brand{left:415px;top:92px;width:155px;text-align:center}
.brand-mark{display:block;width:26px;height:26px;border-radius:50%;background:var(--crimson);margin:0 auto 14px}
.brand-name{font-family:"Oswald",sans-serif;font-weight:500;font-size:10.5px;color:var(--crimson);white-space:nowrap}
.offer{left:428px;top:344px;width:130px;font-size:25px;color:#fff;line-height:1.2}
.site{right:9px;top:498px;font-family:"Oswald",sans-serif;font-size:11px;color:#fff}

/* inside */
.products-title{left:25px;top:27px;font-size:20px;color:var(--crimson)}
.intro{left:25px;top:61px;width:345px;color:var(--body-grey);font-size:7.8px;line-height:10.5px}
.thumb{position:absolute;border-radius:50%;border:1.5px solid var(--crimson)}
.thumb--vest{left:18px;top:118px;width:130px;height:130px;background:radial-gradient(circle,#5b5b5f,#2c2c30 70%,#e9e9ea 71%)}
.thumb--shoes{left:257px;top:290px;width:130px;height:130px;background:radial-gradient(circle at 50% 60%,#2a2a2c,#8d8d90 45%,#f4f4f4 70%)}
.product{position:absolute;width:224px}
.product h3{font-family:"Oswald",sans-serif;font-weight:400;font-size:11.5px;color:var(--orange);margin-bottom:3px}
.product .copy{color:var(--body-grey);font-size:7.4px;line-height:11.5px}
.p1{left:156px;top:114px}.p2{left:156px;top:190px}.p3{left:17px;top:274px}.p4{left:17px;top:350px}
.tagline{left:382px;top:10px;width:155px;text-align:center;font-family:"Oswald",sans-serif;font-size:10px;line-height:1.35;color:#fff}
.sitting-photo{position:absolute;left:575px;top:8px;width:220px;height:150px;background:linear-gradient(160deg,#fff 15%,#b7cbe2 40%,#2b2b30 70%,#fff 92%)}
.why-title{left:430px;top:140px;font-size:18px;color:var(--crimson)}
.reason{position:absolute;left:428px;width:372px;display:flex;gap:18px;align-items:center}
.reason .icon{flex:none;width:40px;height:40px}
.reason .copy{color:var(--body-grey);font-size:7.4px;line-height:11.5px}
.r1{top:180px}.r2{top:245px}.r3{top:310px}
.fabrics{left:18px;top:463px;width:150px;text-align:center;font-family:"Oswald",sans-serif;font-size:12.5px;line-height:1.42;color:var(--ink)}
.quote-mark{left:190px;top:443px;font-family:"Oswald",sans-serif;font-size:30px;color:var(--crimson);line-height:1}
.quote{left:219px;top:455px;width:175px;color:var(--crimson);font-size:7.2px;line-height:10.5px}
.couple-photo{position:absolute;left:425px;top:372px;width:120px;height:155px;background:linear-gradient(180deg,#fff 0%,#c9b29a 25%,#2e2e33 55%,#1a1a1d 100%)}
.cta{right:33px;top:440px;text-align:right;color:#fff}
.cta-line{font-family:"Oswald",sans-serif;font-size:13.5px;line-height:1.3}
.cta-number{font-family:"Oswald",sans-serif;font-size:34px;line-height:1.2}
</style>
</head>
<body>

<section class="sheet sheet--outside">
  <svg class="shapes" viewBox="0 0 814 525" aria-hidden="true">
    <polygon points="205,0 407,0 407,52 240,104" fill="var(--gold)"/>
    <polygon points="211,0 407,0 407,44 246,94" fill="var(--yellow)"/>
    <polygon points="0,368 102,338 268,525 0,525" fill="var(--gold)"/>
    <polygon points="0,377 98,348 258,525 0,525" fill="var(--yellow)"/>
  </svg>

  <div class="block about light">
    <h2 class="heading">About Us</h2>
    <div class="copy">
      <p>Lorem ipsum dolor sit amet, consectetuer adipiscing elit, sed diam nonummy nibh euismod tincidunt ut laoreet dolore magna aliquam erat volutpat. Ut wisi enim ad minim veniam, quis nostrud exerci tation ullamcorper suscipit lobortis nisl ut aliquip ex ea commodo consequat.</p>
      <p>Duis autem vel eum iriure dolor in hendrerit in vulputate velit esse molestie consequat, vel illum dolore eu feugiat nulla facilisis at vero eros et accumsan et iusto odio dignissim qui blandit praesent luptatum zzril delenit augue duis dolore te feugait nulla facilisi. Nam liber tempor cum soluta nobis eleifend option congue nihil imperdiet doming id quod mazim placerat facer possim assum.</p>
      <p>Typi non habent claritatem insitam; est usus legentis in iis qui facit eorum claritatem. Investigationes demonstraverunt lectores legere me lius quod ii legunt saepius. Claritas est etiam processus dynamicus, qui sequitur mutationem consue.</p>
    </div>
  </div>

  <div class="block guarantee">100% SATISFACTION!<br>OR YOUR MONEY BACK.</div>

  <div class="block store light">
    <h2 class="heading">Our Store</h2>
    <div class="copy">
      <p>Lorem ipsum dolor sit amet, consectetuer adipiscing elit, sed diam nonummy nibh euismod tincidunt ut laoreet dolore magna aliquam erat volutpat. Ut wisi enim ad minim veniam, quis nostrud exerci tation ullamcorper suscipit lobortis nisl ut aliquip ex ea commodo consequat.</p>
      <p>Duis autem vel eum iriure dolor in hendrerit in vulputate velit esse molestie consequat, vel illum dolore eu feugiat nulla facilisis at vero eros et accumsan et iusto odio dignissim qui blandit praesent luptatum zzril delenit augue duis dolore te feugait nulla facilisi. Nam liber tempor cum soluta nobis eleifend option congue nihil imperdiet doming id quod mazim placerat facer possim assum.</p>
      <p>Typi non habent claritatem insitam; est usus legentis in iis qui facit eorum claritatem. Investigationes demonstraverunt lectores legere me lius quod ii legunt saepius. Claritas est etiam processus dynamicus, qui sequitur mutationem consue.</p>
    </div>
  </div>

  <div class="block contact">
    <h2 class="heading">Contact Us</h2>
    <div class="contact-row">
      <svg viewBox="0 0 10 12"><path d="M5 0a4 4 0 0 1 4 4c0 3-4 8-4 8S1 7 1 4a4 4 0 0 1 4-4z" fill="var(--crimson)"/><circle cx="5" cy="4" r="1.5" fill="var(--yellow)"/></svg>
      <span>1280 Alder Street #210<br>Vancouver, BC V6B 0A1</span>
    </div>
    <div class="contact-row">
      <svg viewBox="0 0 10 12"><rect x="2" y="0" width="6" height="12" rx="1.2" fill="var(--crimson)"/><rect x="3" y="1.5" width="4" height="7" fill="var(--yellow)"/></svg>
      <span>(604) 555-0173</span>
    </div>
    <div class="contact-row">
      <svg viewBox="0 0 10 12"><rect x="0" y="3" width="10" height="7" fill="var(--crimson)"/><path d="M0 3l5 4 5-4" stroke="var(--yellow)" fill="none"/></svg>
      <span>info@nhsco-example.ca</span>
    </div>
  </div>

  <div class="photo-panel"></div>
  <div class="model-photo" role="img" aria-label="Stock photo of a young man in a black tuxedo with bow tie, adjusting his cuff"></div>

  <div class="block brand">
    <span class="brand-mark"></span>
    <span class="brand-name">Northern Heron Supply Co</span>
  </div>

  <svg class="shapes" viewBox="0 0 814 525" aria-hidden="true">
    <polygon points="407,313 530,278 620,525 407,525" fill="var(--gold)"/>
    <polygon points="407,321 524,288 612,525 407,525" fill="var(--crimson)"/>
    <polygon points="668,525 814,468 814,525" fill="var(--gold)"/>
    <polygon points="682,525 814,476 814,525" fill="var(--crimson)"/>
  </svg>

  <div class="block heading offer">Custom made suits are available from $399 and up</div>
  <div class="block site">www.nhsco-example.ca</div>
</section>

<section class="sheet sheet--inside">
  <svg class="shapes" viewBox="0 0 814 527" aria-hidden="true">
    <polygon points="322,0 628,0 440,112" fill="var(--gold)"/>
    <polygon points="336,0 612,0 442,100" fill="var(--crimson)"/>
    <polygon points="0,432 146,423 186,527 0,527" fill="var(--gold)"/>
    <polygon points="0,440 140,432 176,527 0,527" fill="var(--yellow)"/>
    <polygon points="545,527 608,398 814,388 814,527" fill="var(--gold)"/>
    <polygon points="556,527 616,406 814,396 814,527" fill="var(--crimson)"/>
  </svg>

  <h2 class="block heading products-title">Our Products</h2>
  <p class="block copy intro">Lorem ipsum dolor sit amet, consectetuer adipiscing elit, sed diam nonummy nibh euismod tincidunt ut laoreet dolore magna aliquam erat volutpat. Ut wisi enim ad minim veniam, quis nostrud exerci tation ullamcorper suscipit lobortis nisl ut aliquip ex ea commodo consequat.</p>

  <div class="thumb thumb--vest" role="img" aria-label="Photo of a man wearing a grey vest, shirt and tie"></div>
  <div class="product p1"><h3>PRODUCT 1</h3><p class="copy">Lorem ipsum dolor sit amet, consectetuer adipiscing elit, sed diam nonummy nibh euismod tincidunt ut laoreet dolore magna aliquam erat volutpat. Ut wisi enim ad minim veniam, quis nostrud exerci tation ullamcorper suscipit lobortis nisl ut aliquip ex ea commodo consequat.</p></div>
  <div class="product p2"><h3>PRODUCT 2</h3><p class="copy">Lorem ipsum dolor sit amet, consectetuer adipiscing elit, sed diam nonummy nibh euismod tincidunt ut laoreet dolore magna aliquam erat volutpat. Ut wisi enim ad minim veniam, quis nostrud exerci tation ullamcorper suscipit lobortis nisl ut aliquip ex ea commodo consequat.</p></div>
  <div class="product p3"><h3>PRODUCT 3</h3><p class="copy">Lorem ipsum dolor sit amet, consectetuer adipiscing elit, sed diam nonummy nibh euismod tincidunt ut laoreet dolore magna aliquam erat volutpat. Ut wisi enim ad minim veniam, quis nostrud exerci tation ullamcorper suscipit lobortis nisl ut aliquip ex ea commodo consequat.</p></div>
  <div class="product p4"><h3>PRODUCT 4</h3><p class="copy">Lorem ipsum dolor sit amet, consectetuer adipiscing elit, sed diam nonummy nibh euismod tincidunt ut laoreet dolore magna aliquam erat volutpat. Ut wisi enim ad minim veniam, quis nostrud exerci tation ullamcorper suscipit lobortis nisl ut aliquip ex ea commodo consequat.</p></div>
  <div class="thumb thumb--shoes" role="img" aria-label="Photo of legs in black suit trousers and polished black shoes"></div>

  <div class="block tagline">Custom made suits make the wearer look amazing, as compared to an off the rack suit.</div>
  <div class="sitting-photo" role="img" aria-label="Stock photo of a smiling young man in a blue shirt and tie sitting on the floor"></div>

  <h2 class="block heading why-title">Why Choose Us?</h2>
  <div class="reason r1">
    <svg class="icon" viewBox="0 0 40 40"><circle cx="20" cy="20" r="19" fill="none" stroke="var(--crimson)" stroke-width="1.2"/><rect x="11" y="18" width="4" height="10" fill="var(--crimson)"/><path d="M16 18l4-7c1.5 0 2.5 1 2 3l-1 3h6c1.5 0 2 1 1.7 2.3l-1.7 7.2c-.3 1-1 1.5-2 1.5H16z" fill="var(--crimson)"/></svg>
    <p class="copy">Lorem ipsum dolor sit amet, consectetuer adipiscing elit, sed diam nonummy nibh euismod tincidunt ut laoreet dolore magna aliquam erat volutpat. Ut wisi enim ad minim veniam, quis nostrud exerci tation ullamcorper suscipit lobortis nisl ut aliquip ex ea commodo consequat.</p>
  </div>
  <div class="reason r2">
    <svg class="icon" viewBox="0 0 40 40"><circle cx="20" cy="20" r="19" fill="none" stroke="var(--crimson)" stroke-width="1.2"/><rect x="9" y="13" width="22" height="13" rx="1" fill="none" stroke="var(--crimson)" stroke-width="2"/><circle cx="20" cy="19.5" r="3.2" fill="var(--crimson)"/><rect x="11" y="28" width="18" height="2" fill="var(--crimson)"/></svg>
    <p class="copy">Lorem ipsum dolor sit amet, consectetuer adipiscing elit, sed diam nonummy nibh euismod tincidunt ut laoreet dolore magna aliquam erat volutpat. Ut wisi enim ad minim veniam, quis nostrud exerci tation ullamcorper suscipit lobortis nisl ut aliquip ex ea commodo consequat.</p>
  </div>
  <div class="reason r3">
    <svg class="icon" viewBox="0 0 40 40"><circle cx="20" cy="20" r="19" fill="none" stroke="var(--crimson)" stroke-width="1.2"/><path d="M12 13l5-2 3 5 3-5 5 2v16H12z" fill="var(--crimson)"/><path d="M20 16l-1.5 2 1.5 9 1.5-9z" fill="#fff"/></svg>
    <p class="copy">Lorem ipsum dolor sit amet, consectetuer adipiscing elit, sed diam nonummy nibh euismod tincidunt ut laoreet dolore magna aliquam erat volutpat. Ut wisi enim ad minim veniam, quis nostrud exerci tation ullamcorper suscipit lobortis nisl ut aliquip ex ea commodo consequat.</p>
  </div>

  <div class="block fabrics">Available in Wool, cotton,<br>linen, and a cotton<br>/cashmere blend</div>
  <div class="block quote-mark">&ldquo;</div>
  <p class="block copy quote">Lorem ipsum dolor sit amet, consectetuer adipiscing elit, sed diam nonummy nibh euismod tincidunt ut laoreet dolore magna aliquam erat volutpat. Ut wisi enim ad minim veniam, quis nostrud exerci tation ullamcorper suscipit lobortis nisl ut aliquip ex ea commodo consequat.</p>

  <div class="couple-photo" role="img" aria-label="Stock photo of a young professional man and woman in dark suits"></div>

  <div class="block cta">
    <div class="cta-line">Call us to set up a free appointment<br>to take your measurements!</div>
    <div class="cta-number">604 555 0192</div>
  </div>
</section>

</body>
</html>
```